Business card for a shipping supplies business

Needing a business card design. Please see the logo. The logo with the white font should be used if there is a dark background.

We are looking for the following info on the card. Please see the sample info. We will need the info to be changed with a few different employee names and info but all will use the same template.

Business Name: The Crate Heron
Employee Name : Marcus Delaney
Position: Account Manager
Address: 4827 W. Ridge 418 S.
Fort Worth, TX 73948
email: Marcus@thecrateheron.example
telephone: 855-619-2740 x 207
website: www.getparcelkits.example

Target Market(s)

Businesses who ship products for online sales

Industry/Entity Type

Cardboard

Contact Information for Business Card

Name, title, address, website, logo, telephone number

Font styles to use
Sans Serif

Colors
EE7325
F08F49
F5BC92
FAE3D3
FDF4ED

Requirements
Must have
• Logo on back of card. Clean look, just logo, website address

```html
<!DOCTYPE html>
<html lang="en">
<head>
<meta charset="utf-8">
<title>The Crate Heron — Business Card</title>
<link rel="stylesheet" href="https://fonts.googleapis.com/css2?family=Source+Sans+3:wght@400;700&display=swap">
<style>
  :root {
    --backdrop: #e6e6e6;
    --maroon: #7a2716;
    --orange: #d8652c;
    --orange-text: #e4712f;
    --rule: #b4482a;
    --paper: #f4f4f4;
    --ink: #1c1c1c;
    --white: #ffffff;
  }
  * { box-sizing: border-box; margin: 0; padding: 0; }
  html, body {
    width: 1200px; height: 960px; overflow: hidden;
    background: var(--backdrop);
    font-family: "Source Sans 3", "Source Sans Pro", sans-serif;
  }
  .canvas { position: relative; width: 1200px; height: 960px; }

  .card {
    position: absolute; left: 303px; width: 595px; height: 340px; overflow: hidden;
  }

  /* Front */
  .card-front { top: 120px; background: var(--maroon); }
  .front-mark {
    position: absolute; inset: 0;
    display: flex; flex-direction: column; align-items: center; justify-content: center; gap: 14px;
  }
  .mark-circle {
    width: 110px; height: 110px; border-radius: 50%; background: var(--orange);
  }
  .front-name {
    color: var(--white); font-weight: 700; font-size: 30px; letter-spacing: 0.5px;
  }

  /* Back */
  .card-back { top: 511px; background: var(--maroon); }
  .brand-panel {
    position: absolute; left: 0; top: 0; width: 295px; height: 100%;
    background: var(--paper);
    display: flex; flex-direction: column; align-items: center; justify-content: center; gap: 14px;
    padding-top: 16px;
  }
  .brand-panel .mark-circle { width: 96px; height: 96px; }
  .brand-name { color: var(--ink); font-weight: 700; font-size: 27px; letter-spacing: 0.3px; }
  .divider-bar {
    position: absolute; left: 295px; top: 0; width: 4px; height: 100%; background: var(--orange);
  }
  .rule {
    position: absolute; left: 297px; right: 0; height: 1.5px; background: var(--rule);
  }
  .icon {
    position: absolute; left: 288px; width: 18px; height: 18px; border-radius: 50%;
    background: var(--orange); display: flex; align-items: center; justify-content: center;
  }
  .icon svg { width: 11px; height: 11px; }
  .info {
    position: absolute; left: 327px; color: var(--white); font-size: 15.5px; line-height: 24px;
  }
  .person-name { color: var(--orange-text); font-weight: 700; font-size: 18px; letter-spacing: 0.4px; }
  .website { color: var(--orange-text); font-weight: 700; }
</style>
</head>
<body>
<main class="canvas">

  <section class="card card-front" aria-label="Card front">
    <div class="front-mark">
      <div class="mark-circle"></div>
      <div class="front-name">The Crate Heron</div>
    </div>
  </section>

  <section class="card card-back" aria-label="Card back">
    <div class="brand-panel">
      <div class="mark-circle"></div>
      <div class="brand-name">The Crate Heron</div>
    </div>
    <div class="divider-bar"></div>

    <div class="icon" style="top:86px">
      <svg viewBox="0 0 12 12"><circle cx="6" cy="3.8" r="2.4" fill="#fff"/><path d="M1.5 11.5a4.5 4.5 0 0 1 9 0z" fill="#fff"/></svg>
    </div>
    <div class="info" style="top:83px">
      <div class="person-name">MARCUS DELANEY</div>
      <div>Account Manager</div>
    </div>

    <div class="rule" style="top:141px"></div>

    <div class="icon" style="top:149px">
      <svg viewBox="0 0 12 12"><path d="M6 11.5S2 7 2 4.5a4 4 0 0 1 8 0C10 7 6 11.5 6 11.5z" fill="#fff"/><circle cx="6" cy="4.5" r="1.5" fill="#d8652c"/></svg>
    </div>
    <div class="info" style="top:146px">
      <div>4827 W. Ridge 418 S.</div>
      <div>Fort Worth, TX 73948</div>
    </div>

    <div class="rule" style="top:196px"></div>

    <div class="icon" style="top:213px">
      <svg viewBox="0 0 12 12"><path d="M2.5 1.5l2 0 1 2.5-1.3 1a6 6 0 0 0 2.8 2.8l1-1.3 2.5 1v2a1 1 0 0 1-1 1A9 9 0 0 1 1.5 2.5a1 1 0 0 1 1-1z" fill="#fff"/></svg>
    </div>
    <div class="icon" style="top:237px">
      <svg viewBox="0 0 12 12"><rect x="1" y="2.5" width="10" height="7" fill="none" stroke="#fff" stroke-width="1.2"/><path d="M1 2.5l5 4 5-4" fill="none" stroke="#fff" stroke-width="1.2"/></svg>
    </div>
    <div class="icon" style="top:261px">
      <svg viewBox="0 0 12 12" fill="none" stroke="#fff" stroke-width="1"><circle cx="6" cy="6" r="5"/><ellipse cx="6" cy="6" rx="2.2" ry="5"/><path d="M1 6h10M2 3.3h8M2 8.7h8"/></svg>
    </div>
    <div class="info" style="top:209px">
      <div>855-619-2740 x 207</div>
      <div>Marcus@thecrateheron.example</div>
      <div class="website">www.getparcelkits.example</div>
    </div>
  </section>

</main>
</body>
</html>
```